Italian restaurant needs a flyer to promote wine tasting and wine pairing tours

Need a designer to create one flyer for print and digital use.

(3 pages all either postcard or 1/3 page)Intro page, wine tasting and wine pairing page, wine pairing and cruise page

We are Www.corvalutrattoria.com an top rated Italian restaurant in CABO San Lucas mexico. Our info and history is on the website. We are a fun, cozy bistro ambience that makes you feel like you are in Italy.

Get to know the great tastes of Rome right here in CABO San Lucas at Corvalu Bistro. Farm and sea to table and select national and international wines . We begin with a brief introduction of the restaurant including a quick Salute to the kitchen then sit at our reserved table for a fun and tasty wine food pairing.

Our Founding Chef and In House Sommelier join forces to create four fabulous farm and sea to table dishes, using the freshest ingredients from local sources and only the top wines from small vineyards. Guests are guided through four wine & food pairings, with a some fun facts about wine and the wine producing regions of Mexico. A lively resort casual setting and a night you will never forget.

Wine & Dine Pairing Session includes:
* Welcome cocktail!
* 4-Course Wine Pairing menu
* Each course paired with local wines
* After Tasting Night cap
* Regional history, Wine tasting tips, trivia, and prizes!
* Guests receive 20% off their next reservation
* Everyday at 5:30pm and 9:30pm for one hour and 45 minutes.
* Limited to 10 guests per session please reserve in advance.
* 69usd X person. Tax included .

Target Market(s)

Wine lovers coming to CABO San Lucas

Industry/Entity Type

Restaurant

Font styles to use
Serif

Requirements
Must have
• More image and less text with an elegant yet fun setting
• Must have wine and dine description:
• Get to know the great tastes of Rome right here in CABO San Lucas at Corvalu Bistro. Farm and sea to table and select national and international wines . We begin with a brief introduction of the restaurant including a quick Salute to the kitchen then sit at our reserved table for a fun and tasty wine food pairing.
• Our Founding Chef and In House Sommelier join forces to create four fabulous farm and sea to table dishes, using the freshest ingredients from local sources and only the top wines from small vineyards. Guests are guided through four wine & food pairings, with a some fun facts about wine and the wine producing regions of Mexico. A lively resort casual setting and a night you will never forget.
• Wine & Dine Pairing Session includes:
• * Welcome cocktail!
• * 4-Course Wine Pairing menu
• * Each course paired with local wines
• * After Tasting Night cap
• * Regional history, Wine tasting tips, trivia, and prizes!
• * Guests receive 20% off their next reservation
• * Everyday at 5:30pm and 9:30pm for one hour and 45 minutes.
• * Limited to 10 guests per session please reserve in advance.
• * 69usd X person. Tax included .
• amd must have wine tasting description:
• One hour of fun and flavor!
• Join our in house sommelier in this small group, one hour , lively happy hour party that includes ample tastes of 3 fine wines paired with authentic Italian gourmet appetizers and seasonal menu favorites. Let us share the best of Bajas wines amd perfectly paired tasting menu before hitting the town.
• This Wine Tasting Happy hour includes:
• * Welcome cocktail!
• * 4-Course Tasting menu
• * Each course paired with Baja local wines
• * Starts at 5pm or 6pm. Arrive 5 minutes prior for check in. Space is limited to 20 guests so advanced reservations are recommended.
• * 25usd per person tax included.
• Colors should be like our website www.corvalutrattoria.com
• Files must be editable
Nice to have
• Want this to focus on promoting the restaurant and tours
Should not have
• Errors

```html
<!DOCTYPE html>
<html lang="en">
<head>
<meta charset="utf-8">
<title>Corvalu Bistro – Wine &amp; Dine Brochure</title>
<link href="https://fonts.googleapis.com/css2?family=Cinzel:wght@600&family=Lato:wght@400;700&family=Roboto+Condensed:wght@700&family=Tinos:wght@400;700&display=swap" rel="stylesheet">
<style>
  :root{
    --maroon:#5a0d0d;
    --orange:#f07d0c;
    --ink:#1a1a1a;
    --paper:#ffffff;
    --stone:#e6e6e6;
    --stone-dark:#cfcfcf;
  }
  *{margin:0;padding:0;box-sizing:border-box}
  html,body{width:1200px;height:844px;overflow:hidden;background:var(--paper)}
  .brochure{position:relative;width:1200px;height:844px;font-family:"Lato",sans-serif;color:var(--ink)}
  .shapes{position:absolute;inset:0}
  .panel{position:absolute;top:0;width:400px;height:844px}
  .panel--inside{left:0}
  .panel--contact{left:400px}
  .panel--cover{left:800px}

  .sessions__title{position:absolute;left:32px;top:78px;font-family:"Cinzel",serif;font-weight:600;font-size:23px;line-height:24px;color:var(--maroon);letter-spacing:.5px}
  .sessions__list{position:absolute;left:36px;top:160px;width:340px;list-style:none;font-size:13.5px;line-height:17px}
  .sessions__list li{position:relative;padding-left:18px;margin-bottom:5px}
  .sessions__list li::before{content:"";position:absolute;left:0;top:5px;width:8px;height:8px;border-radius:50%;background:var(--orange)}

  .wordmark{position:absolute;left:0;width:400px;display:flex;align-items:center;justify-content:center;gap:10px;font-family:"Tinos",serif;font-weight:700;color:var(--maroon);letter-spacing:1px}
  .wordmark__dot{width:12px;height:12px;border-radius:50%;background:var(--orange)}
  .panel--contact .wordmark{top:355px;font-size:28px}
  .panel--cover .wordmark{top:110px;font-size:36px}

  .hours{position:absolute;left:0;width:400px;top:478px;text-align:center}
  .hours__lead{font-family:"Tinos",serif;font-size:29px;color:var(--orange)}
  .hours__time{font-family:"Roboto Condensed",sans-serif;font-weight:700;font-size:46px;color:var(--maroon);line-height:54px}

  .contact{position:absolute;left:0;width:400px;top:632px;text-align:center;color:var(--paper)}
  .contact svg{display:block;margin:0 auto}
  .contact__phone{font-size:22px;margin:4px 0 10px}
  .contact__address{font-size:15px;line-height:19px;margin-top:6px}

  .web-pill{position:absolute;left:34px;width:332px;height:34px;border:2px solid var(--ink);border-radius:17px;display:flex;align-items:center;justify-content:center;font-size:15px;letter-spacing:4.2px;color:var(--ink)}
  .panel--contact .web-pill{top:780px;border-color:var(--maroon);color:var(--paper)}
  .panel--cover .web-pill{top:780px;background:var(--paper)}

  .cover-text{position:absolute;left:34px;top:650px;font-family:"Tinos",serif}
  .cover-text__name{font-family:"Cinzel",serif;font-weight:600;font-size:37px;color:var(--maroon);line-height:42px;letter-spacing:.5px}
  .cover-text__kind{font-weight:700;font-size:27px;color:var(--orange);line-height:32px}
  .cover-text__place{font-weight:700;font-size:37px;color:var(--ink);line-height:40px}
</style>
</head>
<body>
<main class="brochure">
  <svg class="shapes" width="1200" height="844" viewBox="0 0 1200 844">
    <defs>
      <linearGradient id="stone" x1="0" y1="0" x2="1" y2="1">
        <stop offset="0" stop-color="#dcdcdc"/><stop offset=".5" stop-color="#f1f1f1"/><stop offset="1" stop-color="#d8d8d8"/>
      </linearGradient>
      <linearGradient id="bottles" x1="0" y1="0" x2="1" y2="1">
        <stop offset="0" stop-color="#5b2418"/><stop offset=".6" stop-color="#2a0e0b"/><stop offset="1" stop-color="#6b3a22"/>
      </linearGradient>
      <linearGradient id="barroom" x1="0" y1="0" x2="0" y2="1">
        <stop offset="0" stop-color="#6a6a6a"/><stop offset="1" stop-color="#2c2c2c"/>
      </linearGradient>
      <radialGradient id="glasses" cx=".5" cy=".5" r=".6">
        <stop offset="0" stop-color="#c79b6a"/><stop offset=".55" stop-color="#8a3b2a"/><stop offset="1" stop-color="#4a2418"/>
      </radialGradient>
      <clipPath id="left-panel"><rect x="0" y="0" width="400" height="844"/></clipPath>
    </defs>

    <rect class="bg-inside" x="0" y="0" width="400" height="844" fill="url(#stone)"/>
    <rect class="bg-contact" x="400" y="0" width="400" height="844" fill="url(#stone)"/>
    <rect class="bg-cover" x="800" y="0" width="400" height="844" fill="var(--paper)"/>

    <g clip-path="url(#left-panel)">
      <circle cx="250" cy="780" r="322" fill="var(--orange)"/>
      <circle cx="250" cy="780" r="314" fill="url(#bottles)" role="img" aria-label="Photo of wine bottles and a decanter on a table"/>
    </g>

    <path d="M400,0 H800 V200 C690,215 560,200 400,72 Z" fill="url(#barroom)" role="img" aria-label="Photo of guests at the bistro bar"/>
    <path d="M400,72 C560,200 690,215 800,200 C900,186 1060,160 1200,205 V232 C1060,190 900,215 800,232 C680,250 540,240 400,112 Z" fill="var(--orange)"/>
    <path d="M800,200 C900,186 1060,160 1200,205 V190 C1060,145 900,170 800,190 Z" fill="var(--maroon)"/>

    <circle cx="1002" cy="425" r="200" fill="var(--orange)"/>
    <circle cx="1002" cy="425" r="193" fill="var(--maroon)"/>
    <circle cx="1002" cy="425" r="183" fill="url(#glasses)" role="img" aria-label="Photo of red wine glasses on a barrel"/>

    <path d="M400,705 C520,640 680,602 800,600 V844 H400 Z" fill="var(--orange)"/>
    <path d="M400,705 C520,640 680,602 800,600" fill="none" stroke="var(--maroon)" stroke-width="6"/>

    <line x1="800" y1="0" x2="800" y2="844" stroke="#bdbdbd" stroke-width="1"/>
    <line x1="400" y1="0" x2="400" y2="844" stroke="#c8c8c8" stroke-width="1"/>
  </svg>

  <section class="panel panel--inside">
    <h2 class="sessions__title">Wine &amp; Dine Pairing<br>Session Includes:</h2>
    <ul class="sessions__list">
      <li>Welcome cocktail!</li>
      <li>4-Course Wine Pairing menu</li>
      <li>Each course paired with local wines After Tasting Night cap</li>
      <li>Regional history, Wine tasting tips, trivia, and prizes!</li>
      <li>Guests receive 20% off their next reservation</li>
      <li>Everyday at 5:30pm and 9:30pm for one hour and 45 minutes.</li>
      <li>Limited to 10 guests per session please reserve in advance.</li>
      <li>69usd X person. Tax included .</li>
    </ul>
  </section>

  <section class="panel panel--contact">
    <div class="wordmark"><span class="wordmark__dot"></span>Corvalu Bistro</div>
    <div class="hours">
      <p class="hours__lead">Open daily from</p>
      <p class="hours__time">5 to 12 am</p>
    </div>
    <div class="contact">
      <svg width="20" height="20" viewBox="0 0 24 24" aria-hidden="true"><path d="M6.6 10.8a15 15 0 0 0 6.6 6.6l2.2-2.2a1 1 0 0 1 1-.25 11.4 11.4 0 0 0 3.6.57 1 1 0 0 1 1 1V20a1 1 0 0 1-1 1A17 17 0 0 1 3 4a1 1 0 0 1 1-1h3.5a1 1 0 0 1 1 1c0 1.25.2 2.45.57 3.57a1 1 0 0 1-.25 1z" fill="var(--maroon)"/></svg>
      <p class="contact__phone">143 5520</p>
      <svg width="18" height="22" viewBox="0 0 24 30" aria-hidden="true"><path d="M12 0a10 10 0 0 0-10 10c0 7.5 10 20 10 20s10-12.5 10-20A10 10 0 0 0 12 0zm0 14a4 4 0 1 1 0-8 4 4 0 0 1 0 8z" fill="var(--maroon)"/></svg>
      <p class="contact__address">Calle Morelos 12, Centro<br>Cabo San Lucas, Mexico</p>
    </div>
    <div class="web-pill">www.corvalutrattoria.com</div>
  </section>

  <section class="panel panel--cover">
    <div class="wordmark"><span class="wordmark__dot"></span>Corvalu Bistro</div>
    <div class="cover-text">
      <h1 class="cover-text__name">Corvalu Bistro</h1>
      <p class="cover-text__kind">ITALIAN RESTAURANT</p>
      <p class="cover-text__place">in Cabo San Lucas</p>
    </div>
    <div class="web-pill">www.corvalutrattoria.com</div>
  </section>
</main>
</body>
</html>
```